Business Card Design job - Tessa's Business Cards

Simple elegant feminine design - Going out on my own as a Mortgage Broker.
My thoughts are the following details on the Front, middle of the card possibly? Phone and email smaller font than my name?
Tessa Marwick
Finance Specialist
p: 0438 217 905
e: tessa@marwickfinance.com.au
Bottom of the card
residential / commercial / equipment
I would like the Font in Rose Gold maybe white or black background? or Possibly a stone grey - are you able to do a few options? I'd like them embossed
Then I had an idea as a simple logo as per the attached if you get the idea in my scribble, my initials, capital T attached to a small m that leads/follows into a circle? Thicker Font In Rose Gold, middle of the card at the back.
Very open to ideas though and what colour you think would look better with the Rose Gold.
Thanks so much for your help, I am not very creative and savvy with this stuff :-)
Industry/Entity Type
Finance
Contact Information for Business Card
Tessa Marwick
p: 0438 217 905
Look and feel
Each slider illustrates characteristics of the customer's brand and the style your logo design should communicate.

```html
<!DOCTYPE html>
<html lang="en">
<head>
<meta charset="utf-8">
<title>Tessa Marwick – Business Cards</title>
<link href="https://fonts.googleapis.com/css2?family=Nunito:ital,wght@1,900&family=Source+Sans+3:wght@200;400;600&family=Oswald:wght@600&display=swap" rel="stylesheet">
<style>
  :root {
    --backdrop: #eceef1;
    --card: #000000;
    --rose-gold: #b8707a;
    --white: #ffffff;
    --rule: #3a3a3a;
  }
  * { margin: 0; padding: 0; box-sizing: border-box; }
  html, body {
    width: 1200px; height: 1200px; overflow: hidden;
    background: var(--backdrop);
  }
  .canvas { position: relative; width: 1200px; height: 1200px; }
  .card {
    position: absolute; left: 156px; width: 888px; height: 522px;
    background: var(--card);
    box-shadow: 3px 4px 8px rgba(0,0,0,0.35);
    font-family: "Source Sans 3", sans-serif;
    color: var(--white);
  }
  .card--front { top: 44px; }
  .card--back { top: 634px; }

  .holder {
    position: absolute; left: 304px; top: 96px; width: 280px; text-align: center;
  }
  .holder__name {
    font-family: "Nunito", sans-serif; font-weight: 900; font-style: italic;
    font-size: 37px; line-height: 1; color: var(--rose-gold); letter-spacing: 0.5px;
    white-space: nowrap;
  }
  .holder__title {
    display: flex; align-items: center; gap: 3px; margin-top: 4px;
    font-weight: 200; font-size: 22px; letter-spacing: 0.3px; white-space: nowrap;
  }
  .holder__title::before, .holder__title::after {
    content: ""; flex: 1; height: 1px; background: #777;
  }

  .contact { position: absolute; left: 305px; top: 280px; font-size: 23px; line-height: 1; }
  .contact__row { margin-bottom: 20px; white-space: nowrap; }
  .contact__label { color: var(--rose-gold); }

  .services {
    position: absolute; left: 0; top: 470px; width: 100%; height: 30px;
    font-size: 22px; letter-spacing: 0.32em; white-space: nowrap;
  }
  .services span { position: absolute; top: 0; }
  .services .divider { color: var(--rose-gold); letter-spacing: 0; }

  .brand {
    position: absolute; left: 0; top: 160px; width: 100%;
    display: flex; flex-direction: column; align-items: center; gap: 14px;
  }
  .brand__mark {
    width: 54px; height: 54px; border-radius: 50%; background: var(--rose-gold);
  }
  .brand__name {
    font-weight: 600; font-size: 34px; color: var(--rose-gold); letter-spacing: 1px;
    white-space: nowrap;
  }
  .role {
    position: absolute; left: 0; top: 386px; width: 100%; text-align: center;
    font-family: "Oswald", sans-serif; font-weight: 600; font-size: 17px; line-height: 1.4;
    letter-spacing: 0.3em; color: var(--rose-gold); white-space: nowrap;
  }
  .role__rule {
    position: absolute; left: 338px; top: 425px; width: 212px; height: 1px; background: var(--rule);
  }
</style>
</head>
<body>
<div class="canvas">
  <section class="card card--front">
    <div class="holder">
      <div class="holder__name">Tessa Marwick</div>
      <div class="holder__title">Finance Specialist</div>
    </div>
    <div class="contact">
      <div class="contact__row"><span class="contact__label">P</span> : 0438 217 905</div>
      <div class="contact__row"><span class="contact__label">E</span> : tessa@marwickfinance.com.au</div>
    </div>
    <div class="services">
      <span style="left:122px">residential</span>
      <span class="divider" style="left:319px">|</span>
      <span style="left:358px">commercial</span>
      <span class="divider" style="left:554px">|</span>
      <span style="left:580px">equipment</span>
    </div>
  </section>

  <section class="card card--back">
    <div class="brand">
      <div class="brand__mark"></div>
      <div class="brand__name">Marwick Finance</div>
    </div>
    <div class="role">MORTGAGE&nbsp; BROKER</div>
    <div class="role__rule"></div>
  </section>
</div>
</body>
</html>
```